Letterhead to Prospective Clients

Create a letterhead (word & canva) that I will use to send letters to prospective clients and also include the Coralwood Estate Partners Logo, My Contact Details and Interchangeable "Suburb". Use the same font and colour pallete

Maris Dulworth | "Suburb" Specialist - Redlands & Surrounds
Mobile: 0417 862 095
Email: MD@CoralwoodEstatePartners.com.au

```html
<!DOCTYPE html>
<html lang="en">
<head>
<meta charset="utf-8">
<title>Coralwood Estate Partners – Letterhead</title>
<link rel="stylesheet" href="https://fonts.googleapis.com/css2?family=Arimo:wght@400;700&display=swap">
<style>
  :root {
    --backdrop: #dcdce0;
    --paper: #ffffff;
    --navy: #0a1b45;
    --sand: #d9a87c;
    --ink: #0f1d45;
  }
  html, body {
    margin: 0;
    padding: 0;
    width: 1200px;
    height: 1179px;
    overflow: hidden;
    background: var(--backdrop);
  }
  .letterhead {
    position: absolute;
    left: 211px;
    top: 39px;
    width: 778px;
    height: 1100px;
    background: var(--paper);
  }
  .letterhead svg { display: block; width: 100%; height: 100%; }
  .header-band { fill: var(--navy); }
  .header-trim { fill: none; stroke: var(--sand); stroke-width: 5; }
  .company-name {
    font-family: "Arimo", Arial, sans-serif;
    font-weight: 400;
    font-size: 30px;
    fill: var(--ink);
  }
  .contact {
    font-family: "Arimo", Arial, sans-serif;
    fill: var(--ink);
    font-size: 16px;
  }
  .contact-name { font-weight: 700; font-size: 19px; }
  .contact-divider { stroke: var(--ink); stroke-width: 1.2; }
</style>
</head>
<body>
  <div class="letterhead">
    <svg viewBox="0 0 1068 1510" preserveAspectRatio="none" xmlns="http://www.w3.org/2000/svg">
      <path class="header-band" d="M0 0 H1068 V72 C900 70 700 42 480 28 C300 18 130 40 0 86 Z"/>
      <path class="header-trim" d="M0 86 C130 40 300 18 480 28 C700 42 900 70 1068 72"/>

      <text class="company-name" x="72" y="198">Coralwood Estate Partners</text>

      <g class="contact" text-anchor="end">
        <text class="contact-name" x="997" y="152">MARIS DULWORTH</text>
        <text x="997" y="171">«Suburb" Specialist - Redlands &amp; Surrounds</text>
        <line class="contact-divider" x1="975" y1="187" x2="997" y2="187"/>
        <text x="997" y="215">Mobile: 0417 862 095</text>
        <text x="997" y="234">Email: MD@CoralwoodEstatePartners.com.au</text>
      </g>
    </svg>
  </div>
</body>
</html>
```